Business Card Design

Kelvarspin

Industry/Entity Type

Business

Contact Information for Business Card

Marrowby Fields Lotto
Marrowby Fields Shopping Centre
Kiosk 3 No.47 Pelican Reach way
Hollinvale North
Dale Ostrowski
0413852276

```html
<!DOCTYPE html>
<html lang="en">
<head>
<meta charset="utf-8">
<title>Marrowby Fields Lotto – Business Card</title>
<link rel="stylesheet" href="https://fonts.googleapis.com/css2?family=Mako&display=swap">
<style>
  :root {
    --navy: #1b2632;
    --sky: #1396c8;
    --title-blue: #1e8fc6;
    --title-grey: #a9adb1;
    --divider: #f2f3f4;
    --ink-dark: #1b2a38;
    --ink-light: #ffffff;
    --backdrop: #e6e7e8;
  }
  html, body {
    margin: 0;
    padding: 0;
    width: 1200px;
    height: 761px;
    overflow: hidden;
    background: var(--backdrop);
  }
  .business-card {
    position: relative;
    width: 1200px;
    height: 761px;
    overflow: hidden;
    font-family: "Mako", sans-serif;
    background: var(--sky);
  }
  .card-bands {
    position: absolute;
    inset: 0;
  }
  .brand-title {
    position: absolute;
    left: 78px;
    top: 92px;
    margin: 0;
    font-size: 64px;
    font-weight: 400;
    letter-spacing: 0.5px;
    color: var(--title-grey);
    white-space: nowrap;
  }
  .brand-title .brand-accent {
    color: var(--title-blue);
  }
  .holder-name {
    position: absolute;
    left: 60px;
    top: 392px;
    margin: 0;
    font-size: 44px;
    font-weight: 400;
    color: var(--ink-dark);
    padding-bottom: 6px;
    border-bottom: 2px solid var(--ink-dark);
    white-space: nowrap;
  }
  .contact-list {
    position: absolute;
    left: 380px;
    top: 382px;
    margin: 0;
    padding: 0;
    list-style: none;
  }
  .contact-item {
    display: flex;
    align-items: flex-start;
    gap: 26px;
    margin-bottom: 30px;
    color: var(--ink-light);
    font-size: 29px;
    line-height: 1.3;
    white-space: nowrap;
  }
  .contact-icon {
    flex: 0 0 56px;
    width: 56px;
    height: 56px;
  }
  .contact-text {
    padding-top: 6px;
  }
</style>
</head>
<body>
  <main class="business-card">
    <svg class="card-bands" width="1200" height="761" viewBox="0 0 1200 761" aria-hidden="true">
      <polygon points="0,0 1200,0 1200,325 0,300" fill="var(--navy)"/>
      <polygon points="0,300 1200,325 1200,352 0,306" fill="var(--divider)"/>
    </svg>

    <h1 class="brand-title"><span class="brand-accent">Marrowby</span> Fields Lotto</h1>

    <p class="holder-name">Dale Ostrowski</p>

    <ul class="contact-list">
      <li class="contact-item">
        <svg class="contact-icon" viewBox="0 0 56 56" aria-label="Address">
          <rect x="3" y="3" width="50" height="50" rx="6" fill="none" stroke="var(--ink-dark)" stroke-width="4"/>
          <path d="M28 44 C20 34 17 29 17 24 a11 11 0 0 1 22 0 c0 5 -3 10 -11 20z" fill="none" stroke="var(--ink-dark)" stroke-width="3.5"/>
          <circle cx="28" cy="24" r="4" fill="var(--ink-dark)"/>
        </svg>
        <span class="contact-text">Marrowby Fields Shopping Centre Kiosk 3 No.47<br>Pelican Reach way Hollinvale North</span>
      </li>
      <li class="contact-item">
        <svg class="contact-icon" viewBox="0 0 56 56" aria-label="Phone">
          <rect x="3" y="3" width="50" height="50" rx="6" fill="none" stroke="var(--ink-dark)" stroke-width="4"/>
          <path d="M20 14 l6 0 l2 8 l-4 3 c2 5 5 8 10 10 l3 -4 l8 2 l0 6 c0 2 -2 3 -4 3 c-14 -1 -24 -11 -25 -25 c0 -2 1 -3 4 -3z" fill="var(--ink-dark)"/>
        </svg>
        <span class="contact-text">0413852276</span>
      </li>
      <li class="contact-item">
        <svg class="contact-icon" viewBox="0 0 56 56" aria-label="Email">
          <rect x="3" y="3" width="50" height="50" rx="6" fill="none" stroke="var(--ink-dark)" stroke-width="4"/>
          <rect x="13" y="14" width="30" height="21" rx="2" fill="none" stroke="var(--ink-dark)" stroke-width="3.5"/>
          <path d="M24 35 l-2 6 h12 l-2 -6" fill="var(--ink-dark)"/>
        </svg>
        <span class="contact-text">daleostrowski@mailnest.com</span>
      </li>
    </ul>
  </main>
</body>
</html>
```